Soap Company Looking To Design New Soap Scent Boxes

we are looking to create a soap box similar to mr brindle. we would like the circle cut out on the top right corner of the box. we are looking for a design that will allow us to use different color base banners for different soap scents (like mr. brindle). we want the soap name scents to be large and readable on the bottom banner (like mr.brindle). we have included our brand figure (logo) and some previous older soap box designs that we were making before the brand figure. the box dims are attached.

```html
<!DOCTYPE html>
<html lang="en">
<head>
<meta charset="utf-8">
<title>Birchwood Bath – Clear Stream Soap Box</title>
<link rel="stylesheet" href="https://fonts.googleapis.com/css2?family=Saira:wght@500;800&family=PT+Serif&display=swap">
<style>
  :root {
    --kraft-light: #e8ddca;
    --kraft-dark: #d9cbb2;
    --scent-blue: #2f58a5;
    --badge-blue: #2c55a3;
    --cutout-blue: #3466b8;
    --cream: #ead6bd;
    --brand-ink: #2b1a14;
    --brand-gold: #f0a91e;
    --page: #ffffff;
  }
  * { box-sizing: border-box; margin: 0; padding: 0; }
  html, body {
    width: 1200px; height: 1200px; overflow: hidden;
    background: var(--page);
  }
  .box-front {
    position: absolute; left: 100px; top: 100px;
    width: 1000px; height: 1000px;
    display: flex; flex-direction: column;
    box-shadow: 0 2px 6px rgba(0,0,0,0.12);
  }
  .kraft-panel {
    position: relative; height: 650px;
    background: linear-gradient(160deg, var(--kraft-light), var(--kraft-dark));
  }
  .organic-tab {
    position: absolute; left: 770px; top: 37px; width: 191px; height: 150px;
  }
  .organic-tab svg { position: absolute; inset: 0; }
  .organic-tab .tab-text {
    position: relative; text-align: center; color: var(--cream);
    font-family: "PT Serif", serif; font-weight: 700; line-height: 1;
    padding-top: 16px;
  }
  .tab-text .pct { font-size: 44px; display: block; }
  .tab-text .word { font-size: 28px; display: block; margin-top: 4px; }
  .window-cutout {
    position: absolute; left: 771px; top: 158px;
    width: 188px; height: 188px; border-radius: 50%;
    background: radial-gradient(circle at 40% 35%, var(--cutout-blue), #2a4f98);
  }
  .brand-mark {
    position: absolute; left: 0; right: 0; top: 130px;
    display: flex; flex-direction: column; align-items: center; gap: 28px;
  }
  .brand-dot {
    width: 230px; height: 230px; border-radius: 50%;
    background: var(--brand-gold);
  }
  .brand-name {
    font-family: "Saira", sans-serif; font-weight: 800;
    font-size: 74px; color: var(--brand-ink); line-height: 1;
  }
  .scent-banner {
    flex: 1; background: var(--scent-blue);
    display: flex; flex-direction: column; align-items: center;
  }
  .scent-name {
    font-family: "Saira", sans-serif; font-weight: 800;
    font-size: 84px; letter-spacing: 3px; color: var(--cream);
    margin-top: 82px; line-height: 1;
  }
  .product-type {
    margin-top: 38px; width: 860px; height: 58px;
    background: var(--cream); color: var(--scent-blue);
    font-family: "Saira", sans-serif; font-weight: 500; font-size: 46px;
    display: flex; align-items: center; justify-content: center; line-height: 1;
  }
  .net-weight {
    margin-top: 32px; font-family: "PT Serif", serif;
    font-size: 26px; color: var(--cream);
  }
</style>
</head>
<body>
  <main class="box-front">
    <section class="kraft-panel">
      <div class="organic-tab">
        <svg width="191" height="150" viewBox="0 0 191 150">
          <polygon points="0,0 191,0 191,150 95.5,118 0,150" fill="var(--badge-blue)"/>
        </svg>
        <div class="tab-text"><span class="pct">100%</span><span class="word">ORGANIC</span></div>
      </div>
      <div class="window-cutout" role="img" aria-label="Die-cut window showing the blue soap bar"></div>
      <div class="brand-mark">
        <div class="brand-dot"></div>
        <div class="brand-name">Birchwood Bath</div>
      </div>
    </section>
    <section class="scent-banner">
      <h1 class="scent-name">CLEAR STREAM</h1>
      <p class="product-type">COLD PRESSED ARTISAN SOAP</p>
      <p class="net-weight">Net Wt. 5oz (140g)</p>
    </section>
  </main>
</body>
</html>
```